Silver Lumen Med Spa Membership Sales Presentation to Clients handout

Hello! We are a high tech, Silver Lumen Med Spa in Dallas Texas that won Best Med Spa in Addison. I want my graphic membership form to represent that. We serve women and men so want it neutral but show cutting edge. Our colors are black, white, gray but would entertain your view. Having a challenge on making it easy to read as each membership gets more services yet one service a month. Thought maybe colorcoding what services are together? Definite road blocks on my end. I used Canva to lay out, but as you can see I am NOT gifted at graphic design. ;))

Target Market(s)

39-69

Industry/Entity Type

Medical Med Spa

Requirements
Must have
• cutting edge look

```html
<!DOCTYPE html>
<html lang="en">
<head>
<meta charset="utf-8">
<title>Ever Radiant Memberships – Silver Lumen Med Spa</title>
<link href="https://fonts.googleapis.com/css2?family=Lato:wght@400;700;900&family=Roboto:wght@400&family=Libre+Baskerville:wght@700&display=swap" rel="stylesheet">
<style>
  :root{
    --backdrop:#46474d;
    --paper:#ffffff;
    --panel:#ebebed;
    --ink:#111111;
    --teal:#4cc8c0;
    --good:#8ee2f0;
    --better:#a5b6f7;
    --best:#4cc8c0;
    --good-mark:#3fbfdc;
    --better-mark:#5468d4;
    --best-mark:#22b3a6;
    --badge:#c0282d;
    --band-1:#9ce6b4;
    --band-2:#b9f1b6;
    --band-3:#d2f8cf;
    --band-4:#bfead9;
    --band-5:#a9d8ea;
    --band-6:#a3c8ee;
    --band-7:#8db2f3;
  }
  *{box-sizing:border-box;margin:0;padding:0}
  html,body{width:1200px;height:1200px;overflow:hidden;background:var(--backdrop)}
  .page{position:absolute;left:253px;top:127px;width:735px;height:951px;background:var(--paper);overflow:hidden;font-family:"Lato",sans-serif;color:var(--ink)}
  .backdrop{position:absolute;left:0;top:0}

  .brand{position:absolute;left:26px;top:116px;width:190px;text-align:center;font-family:"Lato",sans-serif;font-size:12px;font-weight:400;letter-spacing:.3px;color:var(--ink)}
  .title{position:absolute;right:29px;top:20px;text-align:right;font-family:"Roboto",sans-serif;font-weight:400;font-size:43px;line-height:42px;color:var(--ink);letter-spacing:.5px}

  .treatment-head{position:absolute;left:26px;top:141px;width:301px;height:28px;color:#fff;font-weight:900;font-size:17px;letter-spacing:4px;text-align:center;line-height:28px;padding-right:14px}
  .treatment-note{position:absolute;left:26px;top:174px;width:290px;text-align:center;font-style:italic;font-size:14px}

  .tier-label{position:absolute;top:142px;width:75px;height:26px;text-align:center;line-height:26px;font-weight:900;font-size:15px}
  .tier-price{position:absolute;top:168px;width:75px;height:29px;background:#000;color:#fff;text-align:center;line-height:29px;font-weight:900;font-size:15px}
  .col-good{left:463px}.col-better{left:548px}.col-best{left:632px}
  .tier-label.col-good{background:var(--good)}
  .tier-label.col-better{background:var(--better)}
  .tier-label.col-best{background:var(--best)}

  .unlimited-tab{position:absolute;left:24px;top:197px;width:20px;height:101px;background:#000;color:#fff;font-size:11px;font-weight:700;letter-spacing:1px;display:flex;align-items:center;justify-content:center}
  .unlimited-tab span{transform:rotate(-90deg);white-space:nowrap}

  .service-list{position:absolute;left:60px;list-style:none;display:flex;flex-direction:column;justify-content:center;font-size:12.5px;line-height:16.5px;text-transform:uppercase;letter-spacing:.2px}

  .cell{position:absolute;width:75px;background:var(--paper);list-style:none;display:flex;flex-direction:column;justify-content:center;align-items:center;font-size:15px;font-weight:700;line-height:16.5px}
  .cell.col-good{color:var(--good-mark)}
  .cell.col-better{color:var(--better-mark)}
  .cell.col-best{color:var(--best-mark)}

  .discount{position:absolute;top:708px;height:189px;width:75px;display:flex;align-items:center;justify-content:center;padding-top:34px;text-align:center;font-family:"Libre Baskerville",serif;font-weight:700;font-size:21px;line-height:28px;color:var(--ink)}
  .discount.col-good{background:linear-gradient(to bottom,#fff 22%,var(--good))}
  .discount.col-better{background:linear-gradient(to bottom,#fff 22%,var(--better))}
  .discount.col-best{background:linear-gradient(to bottom,#fff 22%,var(--best))}

  .footer{position:absolute;left:0;bottom:0;width:735px;height:40px;background:var(--teal);display:flex;align-items:center;font-size:14.5px;color:var(--ink)}
  .contact{position:absolute;display:flex;align-items:center;gap:8px;white-space:nowrap}
  .contact svg{flex:none}
</style>
</head>
<body>
<main class="page">
  <svg class="backdrop" width="735" height="951" viewBox="0 0 735 951" aria-hidden="true">
    <defs>
      <clipPath id="band-curve">
        <path d="M24 190 L365 190 Q455 560 430 910 L24 910 Z"/>
      </clipPath>
    </defs>
    <polygon points="206,0 735,0 735,121 306,121" fill="var(--teal)"/>
    <rect x="306" y="121" width="429" height="792" fill="var(--panel)"/>
    <path d="M0 121 L306 121 Q475 560 445 913 L0 913 Z" fill="var(--paper)"/>
    <polygon points="26,141 327,141 315,169 26,169" fill="#000"/>
    <circle cx="261" cy="64" r="39" fill="var(--badge)" stroke="#111" stroke-width="3"/>
    <g clip-path="url(#band-curve)">
      <rect x="24" y="197" width="460" height="101" fill="var(--band-1)"/>
      <rect x="24" y="312" width="460" height="122" fill="var(--band-2)"/>
      <rect x="24" y="446" width="460" height="35" fill="var(--band-3)"/>
      <rect x="24" y="491" width="460" height="89" fill="var(--band-4)"/>
      <rect x="24" y="597" width="460" height="28" fill="var(--band-5)"/>
      <rect x="24" y="637" width="460" height="58" fill="var(--band-6)"/>
      <rect x="24" y="708" width="460" height="189" fill="var(--band-7)"/>
    </g>
  </svg>

  <div class="brand">Silver Lumen Med Spa</div>
  <h1 class="title">EVER RADIANT<br>MEMBERSHIPS</h1>

  <div class="treatment-head">TREATMENT</div>
  <p class="treatment-note">(Choose 1 color per month)</p>

  <div class="tier-label col-good">GOOD</div>
  <div class="tier-label col-better">BETTER</div>
  <div class="tier-label col-best">BEST</div>
  <div class="tier-price col-good">$189</div>
  <div class="tier-price col-better">$289</div>
  <div class="tier-price col-best">$389</div>

  <div class="unlimited-tab"><span>UNLIMITED</span></div>

  <ul class="service-list" style="top:197px;height:101px">
    <li>Skin Evaluation</li><li>Infrared Sauna</li><li>Massage Chair</li><li>Vibrational Lymphatic Plate</li><li>Targeted Weight Loss</li>
  </ul>
  <ul class="cell col-good" style="top:203px;height:95px"><li>√</li><li>√</li><li>√</li><li>√</li><li>–</li></ul>
  <ul class="cell col-better" style="top:203px;height:95px"><li>√</li><li>√</li><li>√</li><li>√</li><li>–</li></ul>
  <ul class="cell col-best" style="top:203px;height:95px"><li>√</li><li>√</li><li>√</li><li>√</li><li>√</li></ul>

  <ul class="service-list" style="top:312px;height:122px">
    <li>Medical Facial</li><li>Face Lymphatic Drainage</li><li>Red Light Therapy</li><li>PH Oxygen Serum</li><li>Dermaplaning</li><li>Vitamin A Peel</li>
  </ul>
  <ul class="cell col-good" style="top:312px;height:122px"><li>√</li><li>√</li><li>√</li><li>√</li><li>–</li><li>–</li></ul>
  <ul class="cell col-better" style="top:312px;height:122px"><li>√</li><li>√</li><li>√</li><li>√</li><li>–</li><li>–</li></ul>
  <ul class="cell col-best" style="top:312px;height:122px"><li>√</li><li>√</li><li>√</li><li>√</li><li>√</li><li>√</li></ul>

  <ul class="service-list" style="top:446px;height:35px"><li>Chemical Peel Veluna Italian</li></ul>
  <ul class="cell col-good" style="top:446px;height:35px"><li>–</li></ul>
  <ul class="cell col-better" style="top:446px;height:35px"><li>–</li></ul>
  <ul class="cell col-best" style="top:446px;height:35px"><li>√</li></ul>

  <ul class="service-list" style="top:491px;height:89px">
    <li>Lumora Broadband Light</li><li>Lumora 2 Correction Passes</li><li>Lumora Up To 10 Correction Passes</li><li>Lumora Hair Removal</li>
  </ul>
  <ul class="cell col-good" style="top:491px;height:89px"><li>√</li><li>√</li><li>–</li><li>–</li></ul>
  <ul class="cell col-better" style="top:491px;height:89px"><li>√</li><li>√</li><li>√</li><li>–</li></ul>
  <ul class="cell col-best" style="top:491px;height:89px"><li>√</li><li>√</li><li>√</li><li>√</li></ul>

  <ul class="service-list" style="top:597px;height:28px"><li>Lumora Skin Firm</li></ul>
  <ul class="cell col-good" style="top:597px;height:28px"><li>–</li></ul>
  <ul class="cell col-better" style="top:597px;height:28px"><li>–</li></ul>
  <ul class="cell col-best" style="top:597px;height:28px"><li>√</li></ul>

  <ul class="service-list" style="top:637px;height:58px"><li>Microneedling</li><li>Microneedling PDO Afterglow</li></ul>
  <ul class="cell col-good" style="top:637px;height:58px"><li>–</li><li>–</li></ul>
  <ul class="cell col-better" style="top:637px;height:58px"><li>√</li><li>–</li></ul>
  <ul class="cell col-best" style="top:637px;height:58px"><li>√</li><li>√</li></ul>

  <ul class="service-list" style="top:708px;height:189px">
    <li>Laser Resurfacing</li><li>Trimvale Targeted Weight Loss</li><li>Chemical Peels Progressive or Mid Depth</li><li>Plasma Pen</li><li>Hyperbaric Oxygen</li><li>Massage</li><li>Airbrush Tanning</li><li>Ionic Detox</li><li>Lymphatic Drainage</li><li>Tirzepatide Weight Loss Peptide</li><li>Lip Fillers Needle Less</li>
  </ul>
  <div class="discount col-good">10%<br>OFF</div>
  <div class="discount col-better">20%<br>OFF</div>
  <div class="discount col-best">30%<br>OFF</div>

  <footer class="footer">
    <div class="contact" style="left:14px">
      <svg width="20" height="20" viewBox="0 0 20 20" aria-hidden="true"><circle cx="10" cy="10" r="10" fill="#000"/><path d="M7 5.5c.6-.4 1.2-.2 1.5.4l.7 1.5c.2.5 0 1-.4 1.3l-.6.4c.5 1.2 1.4 2.1 2.6 2.6l.4-.6c.3-.4.8-.6 1.3-.4l1.5.7c.6.3.8.9.4 1.5-.6 1-1.7 1.4-2.8 1-2.5-.9-4.4-2.8-5.3-5.3-.4-1.1 0-2.2 1-2.8z" fill="#fff"/></svg>
      <span>555.014.2200</span>
    </div>
    <div class="contact" style="left:161px">
      <svg width="20" height="20" viewBox="0 0 20 20" aria-hidden="true"><circle cx="10" cy="10" r="10" fill="#000"/><path d="M10 4.5a3.5 3.5 0 0 0-3.5 3.5c0 2.6 3.5 6.8 3.5 6.8s3.5-4.2 3.5-6.8A3.5 3.5 0 0 0 10 4.5zm0 4.8a1.3 1.3 0 1 1 0-2.6 1.3 1.3 0 0 1 0 2.6z" fill="#fff"/></svg>
      <span>118 ALDER DR. ELMRIDGE, TX 75990</span>
    </div>
    <div class="contact" style="left:488px">
      <svg width="20" height="20" viewBox="0 0 20 20" aria-hidden="true"><circle cx="10" cy="10" r="10" fill="#000"/><g fill="none" stroke="#fff" stroke-width="1.1"><circle cx="10" cy="10" r="5"/><ellipse cx="10" cy="10" rx="2.2" ry="5"/><path d="M5 10h10"/></g></svg>
      <span>SILVERLUMENMEDSPA.COM</span>
    </div>
  </footer>
</main>
</body>
</html>
```